依頼詳細
4色(カラー)で角2・長3の封筒のデザインをお願いしたいと思います。
会社のイメージカラーがグリーンとオレンジですので、添付のロゴ(ロゴタイプ)を参考に頂きまして、デザインして頂きたいです。
記載項目
株式会社ソラノ TEL06-6577-2286 FAX06-6577-2287 Freedial 0120-39-4627
〒550-0031 大阪市港区波見台二丁目4番17号ハイツソラノ1F
URL http://www.sorano-kobo.example.jp/
希望イメージ
• +5 0 +5
• シンプル
複雑
• 単色
カラフル
• 暗い
明るい
• 日常
高級
• 遊び心
厳粛
• 未来的
伝統的
• 女性的
男性的
希望する色
緑系、黄・オレンジ系
納品ファイル
• 高解像度JPG (.jpg)
• イラストレーター形式 (.ai)
補足説明
依頼公開後の追記内容
■ 選んだ理由

弊社のイメージカラーを、全体にバランスよくデザイン頂いたように感じました。
コーナーや頭部分のグラデーションもとても綺麗で、白地のロゴやロゴタイプが
引き立つような印象を受けました。
社内でのヒアリングでも1番人気で、殆どの社員がこの作品を気に入っていました。
とても素晴らしいご提案を頂きました。
ありがとうございました。

■ 提案者全員のお礼・コメント

今回初めてQuorvexを利用させて頂きました。
クオーヴァーの皆様には沢山のご提案を頂きまして、ありがとうございました。
弊社の取引のある、代理店やデザイナーに依頼をして今回の依頼内容である
封筒デザインを作成してもらいましたが、どれも完成度が低く満足出来なか
った時にQuorvexを知ることになりました。
ご提案頂いた作品は、どれも完成度が高く単体でご提案頂いた際は問題なく
採用させて頂くレベルのものばかりでした。
また今後も利用させて頂くこともあると思いますので、よろしくお願い致します。
ありがとうございました。

```html
<!DOCTYPE html>
<html lang="ja">
<head>
<meta charset="utf-8">
<title>株式会社ソラノ 封筒デザイン</title>
<link rel="stylesheet" href="https://fonts.googleapis.com/css2?family=Noto+Sans+JP:wght@400;500;700;900&display=swap">
<style>
  :root {
    --bg: #e9eaeb;
    --paper: #ffffff;
    --green: #2e9e3e;
    --green-light: #5cc65a;
    --orange: #ef8a1c;
    --orange-light: #f7b545;
    --ink: #3a3a3a;
    --ink-soft: #6b6b6b;
  }
  * { margin: 0; padding: 0; box-sizing: border-box; }
  html, body { width: 782px; height: 1200px; overflow: hidden; }
  body {
    background: var(--bg);
    font-family: "Noto Sans JP", sans-serif;
    color: var(--ink);
    position: relative;
  }
  .envelope {
    position: absolute;
    left: 88px; top: 30px;
    width: 606px; height: 1140px;
    background: var(--paper);
    overflow: hidden;
  }
  .flap {
    position: absolute; left: 0; top: 0;
    width: 100%; height: 168px;
    background: linear-gradient(180deg, var(--green) 0%, var(--green) 70%, var(--green-light) 100%);
  }
  .flap-name {
    position: absolute;
    right: 150px; top: 56px;
    transform: rotate(180deg);
    color: var(--paper);
    font-weight: 900;
    font-size: 46px;
    letter-spacing: 2px;
    line-height: 1;
  }
  .flap-sub {
    position: absolute;
    right: 200px; top: 30px;
    transform: rotate(180deg);
    color: var(--paper);
    font-weight: 700;
    font-size: 13px;
    letter-spacing: 1px;
  }
  .watermark {
    position: absolute;
    left: 60px; top: 800px;
    width: 270px; height: 270px;
    border-radius: 50%;
    background: radial-gradient(circle, rgba(239,138,28,0.16) 0%, rgba(92,198,90,0.12) 45%, rgba(46,158,62,0.05) 70%, rgba(255,255,255,0) 72%);
  }
  .brand {
    position: absolute;
    left: 28px; top: 1026px;
    display: flex; align-items: center; gap: 10px;
  }
  .brand-dot {
    width: 40px; height: 40px; border-radius: 50%;
    background: var(--orange);
  }
  .brand-name {
    color: var(--green);
    font-weight: 900;
    font-size: 30px;
    letter-spacing: 1px;
    line-height: 1;
  }
  .url {
    position: absolute;
    left: 30px; top: 1100px;
    font-size: 12px;
    color: var(--ink-soft);
  }
  .contact {
    position: absolute;
    left: 300px; top: 1010px;
    width: 290px;
  }
  .freedial { display: flex; align-items: center; gap: 8px; }
  .freedial-number {
    font-size: 34px; font-weight: 500; color: var(--ink);
    line-height: 1; letter-spacing: 0.5px;
  }
  .lines { display: flex; gap: 14px; margin-top: 10px; }
  .line { display: flex; align-items: center; gap: 5px; font-size: 15px; }
  .address {
    display: flex; gap: 5px; margin-top: 9px;
    font-size: 10.5px; color: var(--ink-soft); line-height: 1.5;
  }
  .icon { flex: none; }
</style>
</head>
<body>
  <div class="envelope">
    <div class="flap">
      <div class="flap-name">株式会社ソラノ</div>
      <div class="flap-sub">SORANO Co., Ltd.</div>
    </div>

    <div class="watermark" role="img" aria-label="淡いロゴマークの透かし装飾"></div>

    <div class="brand">
      <span class="brand-dot"></span>
      <span class="brand-name">株式会社ソラノ</span>
    </div>
    <div class="url">http://www.sorano-kobo.example.jp/</div>

    <div class="contact">
      <div class="freedial">
        <svg class="icon" width="38" height="26" viewBox="0 0 38 26">
          <rect x="0" y="0" width="38" height="26" rx="5" fill="var(--orange)"/>
          <path d="M9 8c0 6 5 11 11 11l2-3-3-2-2 1c-2-1-3-2-4-4l1-2-2-3z" fill="#fff"/>
          <circle cx="28" cy="13" r="5" fill="none" stroke="#fff" stroke-width="2"/>
        </svg>
        <span class="freedial-number">0120-39-4627</span>
      </div>
      <div class="lines">
        <div class="line">
          <svg class="icon" width="18" height="16" viewBox="0 0 18 16">
            <rect width="18" height="16" rx="3" fill="var(--orange)"/>
            <path d="M5 4c0 4 3 8 8 8l1-2-2-1-1 1c-2-1-3-2-3-3l1-1-1-2z" fill="#fff"/>
          </svg>
          <span>06-6481-3920</span>
        </div>
        <div class="line">
          <svg class="icon" width="18" height="16" viewBox="0 0 18 16">
            <rect width="18" height="16" rx="3" fill="var(--orange)"/>
            <rect x="4" y="5" width="10" height="7" fill="#fff"/>
            <rect x="6" y="3" width="6" height="3" fill="#fff"/>
          </svg>
          <span>06-6481-3921</span>
        </div>
      </div>
      <div class="address">
        <svg class="icon" width="10" height="14" viewBox="0 0 10 14">
          <path d="M5 0a5 5 0 0 0-5 5c0 4 5 9 5 9s5-5 5-9a5 5 0 0 0-5-5z" fill="var(--orange)"/>
          <circle cx="5" cy="5" r="2" fill="#fff"/>
        </svg>
        <div>〒550-0031<br>大阪市港区波見台二丁目4番17号ハイツソラノ1F</div>
      </div>
    </div>
  </div>
</body>
</html>
```